Design a Small Graphic for a client brochure and Website

We need a a fairly simple diagram/graphic to replace the existing graphic in our brochures and website. We are a Private Wealth Advice firm, dealing with high-end clients. We would like to be able to copyright the final design. We need this design to be stylish and have a long shelf-life.
The original design is quite old and was not updated to reflect our company growth or changes in our website design and brochure designs.
Updates

Target Market(s)

Private Wealth clients
High end
Age 45 plus

Industry/Entity Type

Finance

Font styles to use
Sans Serif
Other font styles liked:
• Stag Sans

Requirements
Must have
• Corporate colours only - plus white
• Pantone 288c (Blue)
• Pantone Cool grey 10c
• Pantone 666c (purple - only limited use for highlighting etc)
• Corporate fonts only
• Stag Sans light, book and thin
• Must provide AI editable files
• Must be able to scale to size and remove/replace any text
• Must be in keeping with our brochures and website which can be viewed at www.lorvane-advisory.com.au
Nice to have
• We want something more vibrant than the image we are using. Something which is in keeping with our image but that is really eye catching.

```html
<!DOCTYPE html>
<html lang="en">
<head>
<meta charset="utf-8">
<title>Lorvane Advisory – Relationship Management Diagram</title>
<link rel="stylesheet" href="https://fonts.googleapis.com/css2?family=Roboto:wght@300;400&display=swap">
<style>
  :root {
    --backdrop: #000000;
    --paper: #ffffff;
    --frame: #8a8d94;
    --navy: #1e2a5a;
    --blue-288: #0a3d80;
    --blue-bright: #3065b0;
    --label: #2a2f6a;
    --heading: #1d4f9c;
    --cool-grey: #4a4d57;
    --purple-666: #a497c8;
    --tagline: #8a6a9a;
  }
  html, body {
    margin: 0;
    width: 1200px;
    height: 1200px;
    overflow: hidden;
    background: var(--backdrop);
  }
  .sheet {
    position: absolute;
    left: 216px;
    top: 57px;
    width: 767px;
    height: 1085px;
    display: block;
  }
  .sheet text { font-family: "Roboto", sans-serif; }
  .brand-name { font-size: 23px; font-weight: 400; fill: var(--navy); }
  .brand-tagline { font-size: 8.5px; font-weight: 400; fill: var(--tagline); letter-spacing: 0.6px; }
  .segment-label { font-size: 18.5px; font-weight: 300; fill: var(--label); }
  .diagram-title { font-size: 28px; font-weight: 300; fill: var(--heading); }
  .swatch-note { font-size: 5px; font-weight: 400; fill: #111; }
  .divider { stroke: var(--label); stroke-width: 1.2; }
</style>
</head>
<body>
<svg class="sheet" viewBox="0 0 697 986" xmlns="http://www.w3.org/2000/svg">
  <rect class="paper" x="0" y="0" width="697" height="986" fill="var(--paper)"/>
  <rect class="page-frame" x="22" y="25" width="650" height="938" fill="none" stroke="var(--frame)" stroke-width="1"/>

  <g class="brand">
    <text class="brand-name" x="645" y="117" text-anchor="end">Lorvane Advisory</text>
    <text class="brand-tagline" x="645" y="129" text-anchor="end">PRIVATE WEALTH ADVISERS</text>
  </g>

  <g class="service-wheel">
    <circle cx="347" cy="473" r="212" fill="none" stroke="var(--navy)" stroke-width="50"/>
    <path class="ring-highlight" fill="var(--blue-bright)"
      d="M584 473 A237 237 0 0 1 339 710 L253.5 635 A187 187 0 0 0 515 391 Z"/>

    <line class="divider" x1="347" y1="288" x2="347" y2="368"/>
    <line class="divider" x1="347" y1="580" x2="347" y2="660"/>
    <line class="divider" x1="162" y1="473" x2="254" y2="473"/>
    <line class="divider" x1="442" y1="473" x2="534" y2="473"/>

    <text class="segment-label" x="267" y="411" text-anchor="middle">Purpose</text>
    <text class="segment-label" x="424" y="411" text-anchor="middle">Investment</text>
    <text class="segment-label" x="424" y="433" text-anchor="middle">Consulting</text>
    <text class="segment-label" x="276" y="549" text-anchor="middle">Wealth</text>
    <text class="segment-label" x="276" y="571" text-anchor="middle">Planning</text>
    <text class="segment-label" x="420" y="549" text-anchor="middle">Your</text>
    <text class="segment-label" x="420" y="571" text-anchor="middle">Legacy</text>
  </g>

  <text class="diagram-title" x="347" y="766" text-anchor="middle">Relationship Management</text>

  <g class="colour-swatches">
    <rect x="38" y="927" width="22" height="23" fill="var(--cool-grey)"/>
    <text class="swatch-note" x="70" y="936">Cool Gray 10 C</text>
    <text class="swatch-note" x="70" y="943">CMYK 40 30 20 66</text>

    <rect x="133" y="927" width="22" height="23" fill="var(--blue-288)"/>
    <text class="swatch-note" x="163" y="936">Pantone 288c (Blue)</text>
    <text class="swatch-note" x="163" y="943">CMYK 100 75 6 24</text>

    <rect x="229" y="927" width="22" height="23" fill="var(--purple-666)"/>
    <text class="swatch-note" x="260" y="936">Pantone 666c</text>
    <text class="swatch-note" x="260" y="943">CMYK 36 39 2 5</text>
  </g>
</svg>
</body>
</html>
```